KORBALT

The business want a professional looking business card. We have a scetch we will add but want the extra upgrade, and would like more suggestions for variations of our business cards.

```html
<!DOCTYPE html>
<html lang="en">
<head>
<meta charset="utf-8">
<title>KORBALT – Business Card</title>
<link rel="stylesheet" href="https://fonts.googleapis.com/css2?family=Lora:wght@400;500&family=Roboto:wght@400&display=swap">
<style>
  :root {
    --backdrop: #141414;
    --card: #ffffff;
    --gold: #c4ac74;
    --gold-deep: #b0975e;
    --card-shadow: rgba(0, 0, 0, 0.45);
  }
  * { margin: 0; padding: 0; box-sizing: border-box; }
  html, body {
    width: 1200px;
    height: 840px;
    overflow: hidden;
    background: var(--backdrop);
  }
  .canvas {
    position: relative;
    width: 1200px;
    height: 840px;
    display: flex;
    align-items: center;
    justify-content: center;
    gap: 60px;
  }
  .card {
    position: relative;
    width: 525px;
    height: 300px;
    background: var(--card);
    box-shadow: 0 12px 30px var(--card-shadow);
    color: var(--gold);
  }

  /* Contact side */
  .contact-card { padding: 46px 48px; }
  .person-name {
    font-family: "Lora", Georgia, serif;
    font-weight: 500;
    font-size: 34px;
    letter-spacing: 0.5px;
    color: var(--gold);
    line-height: 1.1;
  }
  .person-role {
    font-family: "Roboto", Arial, sans-serif;
    font-size: 17px;
    letter-spacing: 1px;
    text-transform: uppercase;
    color: var(--gold);
    margin-top: 6px;
  }
  .contact-list {
    list-style: none;
    margin-top: 34px;
    font-family: "Roboto", Arial, sans-serif;
    font-size: 18px;
    color: var(--gold);
  }
  .contact-item {
    display: flex;
    align-items: center;
    gap: 14px;
    height: 28px;
  }
  .contact-icon {
    width: 18px;
    height: 18px;
    flex: none;
    stroke: var(--gold-deep);
    fill: none;
    stroke-width: 1.6;
  }

  /* Brand side */
  .brand-card {
    display: flex;
    flex-direction: column;
    align-items: center;
    justify-content: center;
  }
  .brand-lockup {
    display: flex;
    align-items: center;
    gap: 16px;
  }
  .brand-dot {
    width: 22px;
    height: 22px;
    border-radius: 50%;
    background: var(--gold);
  }
  .brand-name {
    font-family: "Lora", Georgia, serif;
    font-weight: 500;
    font-size: 40px;
    letter-spacing: 12px;
    color: var(--gold);
  }
  .brand-since {
    font-family: "Roboto", Arial, sans-serif;
    font-size: 12px;
    letter-spacing: 7px;
    text-transform: uppercase;
    color: var(--gold);
    margin-top: 14px;
    margin-left: 38px;
  }
</style>
</head>
<body>
<main class="canvas">

  <section class="card contact-card" aria-label="Business card, contact side">
    <h1 class="person-name">Lars Henrik Solvang</h1>
    <p class="person-role">CEO &amp; Founder</p>
    <ul class="contact-list">
      <li class="contact-item">
        <svg class="contact-icon" viewBox="0 0 18 18" aria-hidden="true">
          <rect x="4.5" y="1.5" width="9" height="15" rx="1.5"/>
          <line x1="8" y1="14" x2="10" y2="14"/>
        </svg>
        <span>004791234567</span>
      </li>
      <li class="contact-item">
        <svg class="contact-icon" viewBox="0 0 18 18" aria-hidden="true">
          <rect x="1.5" y="4" width="15" height="10" rx="1"/>
          <polyline points="1.5,4.5 9,10 16.5,4.5"/>
        </svg>
        <span>korbalt.llc@mailbox.com</span>
      </li>
      <li class="contact-item">
        <svg class="contact-icon" viewBox="0 0 18 18" aria-hidden="true">
          <circle cx="9" cy="9" r="7.5"/>
          <ellipse cx="9" cy="9" rx="3.2" ry="7.5"/>
          <line x1="1.5" y1="9" x2="16.5" y2="9"/>
          <line x1="2.8" y1="5" x2="15.2" y2="5"/>
          <line x1="2.8" y1="13" x2="15.2" y2="13"/>
        </svg>
        <span>www.korbalt.llc</span>
      </li>
    </ul>
  </section>

  <section class="card brand-card" aria-label="Business card, brand side">
    <div class="brand-lockup">
      <span class="brand-dot" aria-hidden="true"></span>
      <span class="brand-name">KORBALT</span>
    </div>
    <p class="brand-since">Since 2026</p>
  </section>

</main>
</body>
</html>
```